Business Card for Dental Surgery

Professional and vibrant business card for dental surgery

Other side to incorporate space for appointment date and times

My website is www.larkvaledental.com.au

Target Market(s)

All

Industry/Entity Type

Dental

Requirements
Must have
• Catchy
Phone no, internet etc
Nice to have
• portray same image as website.
on reverse appointment side:
"Please give 24 hours notice if you cannot attend"
Nice colours

```html
<!DOCTYPE html>
<html lang="en">
<head>
<meta charset="utf-8">
<title>Larkvale Dental – Business Card</title>
<link rel="stylesheet" href="https://fonts.googleapis.com/css2?family=Arimo:ital,wght@0,400;0,700;1,400;1,700&display=swap">
<style>
  :root {
    --purple: #9a4d97;
    --purple-light: #c48bc2;
    --ink: #5f5f5f;
    --ink-soft: #777777;
    --rule: #8a8a8a;
    --paper: #ffffff;
    --stage: #ffffff;
    --photo-a: #f3eeea;
    --photo-b: #d9cfc6;
    --photo-c: #ece8e4;
  }
  * { box-sizing: border-box; margin: 0; padding: 0; }
  html, body { width: 1200px; height: 900px; overflow: hidden; }
  body {
    background: var(--stage);
    font-family: "Arimo", Arial, sans-serif;
    color: var(--ink);
    position: relative;
  }
  .card {
    position: absolute;
    left: 280px;
    width: 700px;
    height: 396px;
    background: var(--paper);
    box-shadow: 4px 5px 8px rgba(0,0,0,0.35);
    overflow: hidden;
  }
  .card--front { top: 30px; }
  .card--back { top: 456px; }

  .front-band {
    position: absolute; left: 0; top: 0; width: 100%; height: 42px;
    background: linear-gradient(90deg, var(--purple) 0%, var(--purple-light) 55%, var(--purple) 100%);
  }
  .front-photo {
    position: absolute; right: 0; top: 42px; width: 300px; height: 354px;
    background: linear-gradient(160deg, var(--photo-a) 0%, var(--photo-b) 45%, var(--photo-c) 100%);
  }
  .wordmark {
    position: absolute;
    font-weight: 700;
    font-size: 44px;
    line-height: 1;
    color: var(--purple);
    letter-spacing: -0.5px;
    white-space: nowrap;
  }
  .card--front .wordmark { left: 24px; top: 74px; }

  .practitioner {
    position: absolute; left: 44px; top: 194px;
    font-size: 21px; font-weight: 700; font-style: italic; color: var(--ink-soft);
  }
  .contact {
    position: absolute; left: 26px;
    font-size: 21px; line-height: 25px; color: var(--ink);
  }
  .contact--address { top: 254px; }
  .contact--phone { top: 322px; font-weight: 700; }
  .contact--web { top: 346px; }
  .contact-row { display: flex; align-items: center; gap: 4px; }
  .contact-row .indent { padding-left: 22px; }
  .contact svg { width: 18px; height: 18px; flex: none; }

  .back-band {
    position: absolute; left: 0; top: 0; width: 44px; height: 100%;
    background: linear-gradient(180deg, var(--purple) 0%, var(--purple-light) 50%, var(--purple) 100%);
  }
  .card--back .wordmark { left: 44px; right: 0; text-align: center; top: 40px; }
  .appointment-label {
    position: absolute; left: 44px; right: 0; top: 140px;
    text-align: center; font-size: 23px; color: var(--ink);
  }
  .appointment-lines {
    position: absolute; left: 80px; top: 186px; width: 590px;
    list-style: none;
  }
  .appointment-lines li {
    height: 28px;
    border-bottom: 2px dotted var(--rule);
  }
  .notice {
    position: absolute; left: 44px; right: 0; top: 338px;
    text-align: center; font-size: 21px; font-style: italic; color: var(--ink-soft);
  }
</style>
</head>
<body>
  <section class="card card--front" aria-label="Business card front">
    <div class="front-band"></div>
    <div class="front-photo" role="img" aria-label="Photo of a smiling young couple"></div>
    <div class="wordmark">Larkvale Dental</div>
    <p class="practitioner">Dr Martin K Hale BDS (Syd)</p>
    <div class="contact contact--address">
      <div class="contact-row">
        <svg viewBox="0 0 18 18" aria-hidden="true"><path d="M2 9 L9 2 L16 9 M4 8 V16 H14 V8" fill="none" stroke="var(--purple)" stroke-width="2.2"/></svg>
        <span>18 Larkvale Road</span>
      </div>
      <div class="contact-row"><span class="indent">Larkvale NSW 2299</span></div>
    </div>
    <div class="contact contact--phone">
      <div class="contact-row">
        <svg viewBox="0 0 18 18" aria-hidden="true"><rect x="5" y="1" width="8" height="16" rx="2" fill="var(--purple)"/><rect x="7" y="4" width="4" height="7" fill="#fff"/></svg>
        <span>02 9555 0142</span>
      </div>
    </div>
    <div class="contact contact--web">
      <div class="contact-row">
        <svg viewBox="0 0 18 18" aria-hidden="true"><circle cx="9" cy="9" r="7" fill="var(--purple)"/><path d="M2 9 H16 M9 2 C5 6 5 12 9 16 C13 12 13 6 9 2" fill="none" stroke="#fff" stroke-width="1.3"/></svg>
        <span>www.larkvaledental.com.au</span>
      </div>
    </div>
  </section>

  <section class="card card--back" aria-label="Business card back">
    <div class="back-band"></div>
    <div class="wordmark">Larkvale Dental</div>
    <p class="appointment-label">Your next appointment:</p>
    <ul class="appointment-lines">
      <li></li><li></li><li></li><li></li>
    </ul>
    <p class="notice">Please give 24 hours notice if you cannot attend</p>
  </section>
</body>
</html>
```